Concept design for a tea business Labels

Hello, we are looking for concepts for our label/packaging for a tea business that has been in business now for over a year. We are a beachy, organic, "It's your moment. Enjoy it." type tea business. We have an online website (www.corvalbrewhouse.com.au) and sell at local markets around the Tarrowby Cove area.
We are looking to upgrade our label to look more professional, in a fun/beachy/chilled out style. (unlike the traditional tea labels).
We do loose leaf tea and iced tea consentrated syrups. We have a few different packages (please see website under "sizes and packaging" bottom left). We would like to experiement with various different size and shape of labels for different products, so would like a concept design for a label using our logo (see website front page bottom). There are no colour constraints.
We use the Quillan brand labels of the following sizes:
1. Pure Glass Rectangular Product Labels, Q4825, 100/Pack, 96 x 50.8 mm
2. Pure Glass Round Multi-purpose Labels, Q3907D, 240/Pack, 40 mm diameter
3.Pure Glass Square Product Labels, Q4861, 350/Pack, 35 x 35 mm
4. For bottles we use Grained Ivory Curved Labels, Q4839, 90/Pack, 57.2 x 77 mm
If you have any more questions, please don't hesitate to contact me
Updates
Hi All,
I am considering using a box like below for packing and doing a bit of a white/beachy feel to the packaging. Either using the rectangle or round circle labels. (circle labels from quillan 60mm diameter).

Reason: Hi All - Thank you so much for all your designs. While I have seen some really beautiful designs I am excited about, it seems there was a rush at the end with a number of new designs just submitted. I still haven't seen just one design I love for the label, so I would like the opportunity to work with some of the new designers to see if we can modify to suit the concept.
Would anyone like to try a concept label with a silhouette of one of the following wave/beach/teacup? I'm just exploring a different approach as I know it is difficult tying in the beach with tea - please think - chilled out beach hut with tea/iced tea, sunrise over ocean. I like the soft colour palette - beachy feel to it - ie. Pastels - blues, greens, whites, sandy, pinks, purples, greys - sunrises over ocean, maybe a white rustic wood feel - or any other icon from Tarrowby Cove - like the Norfolk Pine's along the beach - maybe in Silhouette.
Just some more ideas.
Thank you again for all your contributions!
Petra

```html
<!DOCTYPE html>
<html lang="en">
<head>
<meta charset="utf-8">
<title>Tarrowby Tea Company – Label Design Concept 1</title>
<link rel="stylesheet" href="https://fonts.googleapis.com/css2?family=Arimo:wght@400;700&family=Tinos:ital@1&family=Maven+Pro:wght@400;700&display=swap">
<style>
  :root {
    --sand: #efe3cc;
    --plum: #5b2a45;
    --white: #ffffff;
    --ink: #4a4346;
    --ink-soft: #7a7275;
    --caption: #cfc5bd;
    --band-shadow: rgba(60, 30, 20, 0.18);
  }
  * { box-sizing: border-box; margin: 0; padding: 0; }
  html, body { width: 1200px; height: 900px; overflow: hidden; }
  body { background: var(--sand); font-family: "Arimo", Arial, sans-serif; position: relative; }

  .stage { position: absolute; left: 0; top: 0; width: 1200px; height: 800px; }

  /* Round product label */
  .round-label {
    position: absolute; left: 120px; top: 170px;
    width: 320px; height: 320px; border-radius: 50%;
    background: var(--plum); overflow: hidden;
    box-shadow: 0 6px 18px var(--band-shadow);
    color: var(--white); text-align: center;
  }
  .round-label .mark-dot {
    width: 54px; height: 54px; border-radius: 50%;
    border: 3px solid var(--white); margin: 52px auto 16px;
  }
  .round-label .brand-name {
    font-weight: 700; font-size: 30px; line-height: 1.05; letter-spacing: 0.5px;
  }
  .round-label .brand-name span { display: block; font-size: 24px; letter-spacing: 2px; }
  .round-label .tea-name { font-size: 17px; margin-top: 16px; font-weight: 700; }
  .round-label .organic-band {
    position: absolute; left: 0; right: 0; bottom: 0; height: 66px;
    background: var(--white);
  }
  .round-label .organic-band p {
    font-family: "Tinos", Georgia, serif; font-style: italic;
    color: var(--plum); font-size: 20px; padding-top: 10px;
  }

  /* Rectangular product label */
  .rect-label {
    position: absolute; left: 560px; top: 170px;
    width: 500px; height: 265px; background: var(--white);
    box-shadow: 0 6px 18px var(--band-shadow);
    color: var(--ink);
  }
  .rect-label .header {
    height: 70px; background: var(--plum); color: var(--white);
    display: flex; align-items: center; padding: 0 20px; gap: 12px;
    position: relative;
  }
  .rect-label .header .mark-dot {
    width: 34px; height: 34px; border-radius: 50%; border: 2px solid var(--white);
  }
  .rect-label .header .brand-name { font-weight: 700; font-size: 22px; letter-spacing: 0.5px; }
  .rect-label .header .organic {
    position: absolute; right: 20px; bottom: 8px;
    font-family: "Tinos", Georgia, serif; font-style: italic; font-size: 14px;
  }
  .rect-label .content { padding: 14px 20px 0; }
  .rect-label .tea-name { font-size: 20px; margin-bottom: 8px; }
  .rect-label .intro, .rect-label .steep, .rect-label .story { font-size: 11px; line-height: 1.45; margin-bottom: 7px; }
  .rect-label .steep { font-weight: 700; }
  .rect-label .story { color: var(--ink-soft); }
  .rect-label .web { font-size: 11px; margin-top: 6px; }
  .rect-label .address { font-size: 9px; color: var(--ink-soft); margin-top: 3px; }

  /* Small round seal sticker */
  .seal-sticker {
    position: absolute; left: 740px; top: 520px;
    width: 150px; height: 150px; border-radius: 50%;
    background: var(--plum); color: var(--white);
    display: flex; align-items: center; justify-content: center; text-align: center;
    box-shadow: 0 6px 18px var(--band-shadow);
    font-weight: 700; font-size: 17px; line-height: 1.15;
  }

  .caption-bar {
    position: absolute; left: 0; top: 800px; width: 1200px; height: 100px;
    background: var(--white); padding: 40px 0 0 34px;
    font-family: "Maven Pro", Arial, sans-serif; color: var(--caption);
    font-size: 29px; letter-spacing: 1px;
  }
  .caption-bar strong { font-weight: 700; }
</style>
</head>
<body>
  <main class="stage">
    <section class="round-label" aria-label="Round product label">
      <div class="mark-dot"></div>
      <h1 class="brand-name">TARROWBY TEA<span>COMPANY</span></h1>
      <p class="tea-name">Black Tea – Australian</p>
      <div class="organic-band"><p>organic</p></div>
    </section>

    <section class="rect-label" aria-label="Rectangular product label">
      <header class="header">
        <div class="mark-dot"></div>
        <h2 class="brand-name">TARROWBY TEA COMPANY</h2>
        <span class="organic">organic</span>
      </header>
      <div class="content">
        <h3 class="tea-name">Black Tea – Australian</h3>
        <p class="intro">An Australian black tea grown in Queensland. Keep Fresh. Enjoy.</p>
        <p class="steep">Steep tea leaves with boiling water for 3–5 minutes.</p>
        <p class="story">Tarrowby Tea Company is about you. It's your moment, enjoy it. Steeped by the sea, our leaves are blended slowly for calm mornings and warm afternoons, so every cup feels like a quiet walk along the shore.</p>
        <p class="web">www.corvalbrewhouse.com.au</p>
        <p class="address">PO Box 218, Tarrowby Cove NSW 2099</p>
      </div>
    </section>

    <section class="seal-sticker" aria-label="Round seal sticker">
      <p>TARROWBY<br>TEA<br>COMPANY</p>
    </section>
  </main>

  <footer class="caption-bar">LABEL DESIGN - <strong>CONCEPT 1. (3)</strong> usage</footer>
</body>
</html>
```